Sports Event Company designing web home page

Design a home page for a Sports event company. Our company is launching an innovative new sports event (quite similiar to adult tag rugby) and we need a slick , kool , innovative website to help us launch our event . Our website needs to portray us as an energetic sports company but yet give a level of professionalism and reassurance despite our product been new.

We have built a Registration system but have encountered that the better website developers are not necessarilt the best designers.

Target Market(s)

20 to 35 year olds who are sporty . Sports and social commitees from corporates

Industry/Entity Type

Adult

Requirements
Must have
• Strong ability to interact with social media

Easy to register for events

Bright but classy

Colour scheme transferrable to Flyers , posters etc

```html
<!DOCTYPE html>
<html lang="en">
<head>
<meta charset="utf-8">
<title>Tag Rovers</title>
<link href="https://fonts.googleapis.com/css2?family=PT+Sans&family=Arimo:wght@400&display=swap" rel="stylesheet">
<style>
:root{
  --bar:#2a2a2c;
  --header:#232325;
  --page:#1e1e1f;
  --panel:#3d3d3d;
  --footer:#1a1a1b;
  --red:#c8232c;
  --red-dark:#a3161e;
  --white:#ffffff;
  --text:#b4b4b4;
  --muted:#9a9a9a;
  --heading:#d6d6d6;
  --orange:#f0a020;
  --field:#efede6;
  --stage:#e8e8e8;
  --icon:#6d6d70;
}
*{margin:0;padding:0;box-sizing:border-box}
html,body{width:1031px;height:1200px;overflow:hidden;background:var(--page)}
.canvas{position:relative;width:1000px;height:1164px;transform:scale(1.031);transform-origin:0 0;font-family:"Arimo",Arial,sans-serif;color:var(--text)}
.abs{position:absolute}
.top-bar{left:0;top:0;width:1000px;height:52px;background:var(--bar)}
.social{display:flex;gap:18px}
.social span{width:22px;height:22px;border-radius:3px;background:var(--icon)}
.search{left:769px;top:12px;width:206px;height:30px;border-radius:5px;background:var(--white);border:1px solid #bbb;font-size:13px;color:#555;padding:8px 0 0 16px}
.search svg{position:absolute;right:12px;top:6px}
.header{left:0;top:52px;width:1000px;height:86px;background:var(--header);border-bottom:2px solid var(--red-dark)}
.brand{left:58px;top:14px;font-family:"PT Sans",sans-serif;font-size:36px;color:var(--white);white-space:nowrap}
.nav{left:424px;top:19px;display:flex;height:40px}
.nav a{display:block;height:40px;line-height:40px;padding:0 12px;font-family:"PT Sans",sans-serif;font-size:14px;color:#e2e2e2;text-decoration:none;white-space:nowrap;background:linear-gradient(#3c3c3e,#29292b);border-left:1px solid #1a1a1a;border-right:1px solid #4a4a4c}
.nav a.active{background:linear-gradient(#d8333b,var(--red-dark));color:var(--white);padding:0 17px}
.stage{left:0;top:140px;width:1000px;height:350px;background:linear-gradient(#f1f1f1,var(--stage))}
.slider-frame{left:37px;top:20px;width:921px;height:310px;background:var(--white);border:1px solid #d0d0d0;box-shadow:0 8px 14px rgba(0,0,0,.18)}
.slide{left:10px;top:10px;width:900px;height:290px;background:linear-gradient(#6e7370 0%,#7f8a80 35%,#4f7d3a 60%,#3f6d2c 100%)}
.arrow{top:127px;width:28px;height:36px;background:rgba(255,255,255,.75)}
.caption{left:0;top:232px;width:900px;height:58px;background:rgba(30,30,30,.75);color:var(--white);font-family:"PT Sans",sans-serif;font-size:13px;line-height:18px;padding:11px 90px 0 49px}
.dots{left:388px;top:262px;width:126px;height:28px;background:#dcdcdc;border-radius:6px 6px 0 0;display:flex;gap:7px;padding:8px 0 0 9px}
.dots i{width:12px;height:12px;border-radius:50%;background:#9c9c9c;box-shadow:inset 0 1px 2px rgba(0,0,0,.4)}
.dots i.on{background:#e0585c}
.panel{background:var(--panel)}
.panel-title{font-size:19px;color:var(--white)}
.reg label{position:absolute;font-size:12px;color:var(--white);width:56px;text-align:right}
.reg .input{position:absolute;left:61px;width:184px;height:26px;border-radius:13px;background:var(--field);box-shadow:inset 0 2px 3px rgba(0,0,0,.25)}
.submit{left:160px;top:170px;width:82px;height:30px;border-radius:15px;background:#111;color:var(--white);font-size:13px;text-align:center;line-height:30px}
.news-item{left:8px;width:254px;font-size:11px;line-height:13px;color:var(--white)}
.news-date{color:var(--orange);font-size:11px}
.read{color:var(--orange);font-size:11px}
.sep{left:0;width:269px;border-top:1px dotted #777}
.section-title{font-size:15px;color:var(--heading);white-space:nowrap}
.body-text{font-size:12.5px;line-height:24px;color:var(--muted)}
.small-text{font-size:11px;line-height:18px;color:var(--muted)}
.photo{border:1px solid #888}
.footer{left:0;top:1084px;width:1000px;height:80px;background:var(--footer);border-top:1px solid #2e2e2e}
.footer-links{left:533px;top:30px;font-size:12px;color:var(--muted);white-space:nowrap}
</style>
</head>
<body>
<div class="canvas">

  <div class="abs top-bar">
    <div class="abs social" style="left:553px;top:16px" aria-label="Social links">
      <span></span><span></span><span></span><span></span><span></span>
    </div>
    <div class="abs search">Search
      <svg width="20" height="20" viewBox="0 0 20 20"><circle cx="8" cy="8" r="6" fill="none" stroke="#777" stroke-width="2"/><path d="M12.5 12.5l5 5" stroke="#777" stroke-width="3"/></svg>
    </div>
  </div>

  <header class="abs header">
    <div class="abs brand">Tag Rovers</div>
    <nav class="abs nav">
      <a class="active" href="#">Home</a><a href="#">Services</a><a href="#">Playing Game</a><a href="#">About us</a><a href="#">News</a><a href="#">Gallery</a><a href="#">Contact us</a>
    </nav>
  </header>

  <section class="abs stage">
    <div class="abs slider-frame">
      <div class="abs slide" role="img" aria-label="Adult tag players in bibs training on a grass pitch in front of a stand">
        <div class="abs arrow" style="left:0"><svg width="28" height="36"><path d="M17 11l-7 7 7 7" fill="none" stroke="#fff" stroke-width="3"/></svg></div>
        <div class="abs arrow" style="left:872px"><svg width="28" height="36"><path d="M11 11l7 7-7 7" fill="none" stroke="#fff" stroke-width="3"/></svg></div>
        <div class="abs caption">Sed ut perspiciatis unde omnis iste natus error sit voluptatem accusantium doloremque laudantium, totam rem aperiam, eaque ipsa quae ab illo inventore veritatis et quasi architecto</div>
        <div class="abs dots"><i></i><i></i><i class="on"></i><i></i><i></i><i></i></div>
      </div>
    </div>
  </section>

  <aside class="abs panel reg" style="left:18px;top:507px;width:269px;height:213px">
    <svg class="abs" style="left:20px;top:8px" width="26" height="30" viewBox="0 0 26 30"><path d="M4 26L20 4l3 2L7 28z" fill="#eee"/><path d="M2 28h22" stroke="#999" stroke-width="1.5"/></svg>
    <div class="abs panel-title" style="left:58px;top:16px">Register</div>
    <label style="left:0;top:64px">Name :</label><div class="input" style="top:57px"></div>
    <label style="left:0;top:101px">E - mail :</label><div class="input" style="top:94px"></div>
    <label style="left:0;top:142px">Phone :</label><div class="input" style="top:131px"></div>
    <div class="abs submit">Submit</div>
  </aside>

  <aside class="abs panel" style="left:18px;top:747px;width:269px;height:317px">
    <svg class="abs" style="left:20px;top:12px" width="28" height="30" viewBox="0 0 28 30"><rect x="3" y="5" width="18" height="22" fill="#ddd" transform="rotate(-10 12 16)"/><rect x="7" y="4" width="18" height="22" fill="#f4f4f4"/><path d="M10 10h12M10 14h12M10 18h12M10 22h8" stroke="#888"/></svg>
    <div class="abs panel-title" style="left:58px;top:17px">Latest News</div>
    <div class="abs news-item" style="top:63px"><div class="news-date">23/02/2012</div><div style="margin-top:14px">Fieldline by Northbrook for a further 5 years</div><div style="margin-top:13px">Fieldline has been reappointed for 2013-2017 to The Riverside Lawn Games Club's Overseas Tour and Hospitality programmeNow in its 20th...</div></div>
    <div class="abs sep" style="top:166px"></div>
    <div class="abs news-item" style="top:178px"><div class="news-date">23/02/2012</div><div style="margin-top:14px">Fieldline by Northbrook for a further 5 years</div><div style="margin-top:13px">Fieldline has been reappointed for 2013-2017 to The Riverside Lawn Games Club's Overseas Tour and Hospitality programmeNow in its 20th...</div></div>
    <div class="abs read" style="left:202px;top:293px">Read More</div>
  </aside>

  <main>
    <h1 class="abs section-title" style="left:322px;top:521px;font-weight:400">WELCOME TO TAG ROVERS</h1>
    <div class="abs" style="left:321px;top:559px;width:353px;height:198px;background:#000">
      <div class="abs" style="left:4px;top:4px;width:343px;height:174px;background:linear-gradient(#8d8c86,#5b6b55 60%,#3e5a30)" role="img" aria-label="Video still of two players contesting the ball at a training session"></div>
      <svg class="abs" style="left:158px;top:83px" width="40" height="40"><circle cx="20" cy="20" r="19" fill="rgba(40,40,40,.6)" stroke="#ddd" stroke-width="2"/><path d="M15 11l13 9-13 9z" fill="#eee"/></svg>
      <div class="abs" style="left:4px;top:181px;width:343px;height:12px;background:#1c1c1c">
        <svg class="abs" style="left:6px;top:2px" width="8" height="8"><rect width="3" height="8" fill="#ddd"/><rect x="5" width="3" height="8" fill="#ddd"/></svg>
        <div class="abs" style="left:26px;top:4px;width:276px;height:4px;background:#444"></div>
      </div>
    </div>
    <p class="abs body-text" style="left:683px;top:578px;width:308px">Nunc varius facilisis eros. Sed erat. In in velit quis arcu ornare laoreet. Curabitur adipiscing luctus massa.Integer ut purus ac augue commodo . Nunc nec mi eu justo tempor consectetuer. Etiam vitae nisl. In dignissim lacus ut ante. Cras elit lectus, bibendum a, adipiscing vitae, commodo et, dui.</p>
    <p class="abs body-text" style="left:328px;top:772px;width:660px">Lorem ipsum dolor sit amet, consectetuer adipiscing elit. Nam nibh. Nunc varius facilisis eros. Sed erat. In in velit quis arcu ornare laoreet. Curabitur adipiscing luctus massa.Lorem ipsum dolor sit amet, consectetuer adipiscing elit. Nam nibh. Nunc varius facilisis eros. Sed erat. In in velit quis arcu ornare laoreet. Curabitur luctus massa.</p>
    <div class="abs" style="left:330px;top:855px;width:653px;border-top:1px dotted #666"></div>

    <h2 class="abs section-title" style="left:328px;top:876px;font-size:13px;font-weight:400">TOP EVENTS</h2>
    <div class="abs photo" style="left:326px;top:902px;width:220px;height:94px;background:linear-gradient(#5a5048,#3e3a3a 50%,#6c6458)" role="img" aria-label="Aerial view of a large stadium at dusk"></div>
    <p class="abs small-text" style="left:328px;top:998px;width:225px">Lorem ipsum dolor sit amet, consectetuer adipiscing elit. Nam nibh. Nunc varius facilisis eros. Sed erat.</p>
    <div class="abs read" style="left:331px;top:1058px">Read More</div>

    <h2 class="abs section-title" style="left:597px;top:878px;font-size:13px;font-weight:400">LATEST EVENTS</h2>
    <div class="abs photo" style="left:597px;top:902px;width:116px;height:94px;background:linear-gradient(#777,#555 40%,#4f7e3a 60%)" role="img" aria-label="Player running with the ball in an empty stadium"></div>
    <div class="abs photo" style="left:727px;top:902px;width:116px;height:94px;background:linear-gradient(#8a8a80,#5e7a4a 55%,#4a7434)" role="img" aria-label="Two players contesting the ball in a match"></div>
    <div class="abs photo" style="left:857px;top:902px;width:116px;height:94px;background:linear-gradient(#8a8d88,#5f7f4e 50%,#4d7a38)" role="img" aria-label="Players chasing the ball across a pitch"></div>
    <p class="abs small-text" style="left:603px;top:1000px;width:100px">Lorem ipsum dolor sit amet.</p>
    <p class="abs small-text" style="left:729px;top:1000px;width:100px">Lorem ipsum dolor sit amet.</p>
    <p class="abs small-text" style="left:859px;top:1000px;width:100px">Lorem ipsum dolor sit amet.</p>
    <div class="abs read" style="left:606px;top:1042px">Read More</div>
    <div class="abs read" style="left:731px;top:1042px">Read More</div>
    <div class="abs read" style="left:862px;top:1042px">Read More</div>
  </main>

  <footer class="abs footer">
    <div class="abs social" style="left:32px;top:26px" aria-label="Social links">
      <span></span><span></span><span></span><span></span><span></span>
    </div>
    <div class="abs footer-links">Privacy &nbsp;&nbsp;|&nbsp;&nbsp; Disclaimer &nbsp;&nbsp;|&nbsp;&nbsp; Contact Us <span style="margin-left:30px">© 2012 Tag Rovers &nbsp;&nbsp;All rights reserved</span></div>
  </footer>

</div>
</body>
</html>
```